New CORPORATE WEBSITE DESIGN (Graphic layout for a WEBSITE TEMPLATE required - Photoshop files)

Hi – I need a draft created for a new corporate website for our company.
I need a graphic design concept which can be applied to a whole website layout -
I have a separate web development team who will implement the design onto Wordpress.
We are an Asian Buying Office based in Hong Kong and Shenzhen which facilitates relationships between factories in China and customers (retailers/etailers) all over the world.
We are a “boutique” agency, which offers highly customized services – we are highly consultative in our approach and tailor services to suit the needs of our customers with customized solutions. Our services are transparent partnership- and-integrity-based, and aimed to support at a certain size of company in growth mode.
We have dedicated teams of staff focused entirely on a customer’s business and we work TOGETHER with customers to solve their product design, patent, product engineering, goods production, quality control and supply chain challenges operating in 24/7 through our proprietary web-based supply chain platform called Cargoloom.
I have a PowerPoint which can be used to drive:
1) creative direction (colour palette etc) and to provide basic content for each “screen.” I would like to see design options based on the PowerPoint which offer creative ways to create a new look and feel for us for a corporate website which will not be social media enabled or ecommerce enabled. We do not put ANY customer brand names direct or references on our website – relationships are private. The home page of the website should say in the design style – “product design and branded global consumer goods” as well as “professional engineering and quality control proficiency”.
The website should be clean and functional – have the “usability” of the Vexor website but the “Calder 400” look & feel of the Oro & Tazz website (http://www.orotazz.com/eng/global/home.php) – Oro & Tazz is a benchmark for us. Oro & Tazz is the largest company in our industry doing what we do.
I do not want to COPY this example - I am offering it as a benchmark for a CLEAN, vibrant, professional site which sends a good brand and services message. The target market is a global B to B market – SMEs who are well funded and growing, brands with growth potential, or large, established brands who are looking to a) build a supply chain partner to help them grow b) increase their revenues by managing their costs c) reduce their risk through an experience buyer’s agent such as ourselves – a partner with integrity who they can trust. The web site design must say “global consumer brands” WITHOUT DIRECTLY ALLUDING TO THE LOGOS AND/OR BRAND NAMES WE WORK WITH , " full service agency – managing the process from product design and engineering, quality control and risk management to product manufacturing and shipping logistics" and “accountability/integrity/transparency within the partnership.” Designer to choose colors to be used in the design - I have also attached my logo file to allow you to select a color palette which will be complementary.
PLEASE FEEL FREE TO ASK ANY QUESTIONS - I AM HAPPY TO PROVIDE MORE DETAILS.
Described in the Project Description.
Graphic Design

```html
<!DOCTYPE html>
<html lang="en">
<head>
<meta charset="utf-8">
<title>Orvane</title>
<link href="https://fonts.googleapis.com/css2?family=Questrial&family=Ubuntu:wght@300;400;500;700&display=swap" rel="stylesheet">
<style>
  :root {
    --page-bg: #f3f3f3;
    --panel-bg: #ffffff;
    --panel-line: #e2e2e2;
    --navy: #0f0a62;
    --navy-dark: #07034a;
    --navy-light: #1d1678;
    --heading: #16107a;
    --subheading: #4b4199;
    --body-text: #7a7a7a;
    --dark-text: #2a2a2a;
    --footer-text: #6b6b6b;
    --dot: #9a9a9a;
  }
  * { box-sizing: border-box; margin: 0; padding: 0; }
  html, body { width: 1200px; height: 1015px; overflow: hidden; }
  body { background: var(--page-bg); font-family: "Ubuntu", sans-serif; color: var(--body-text); position: relative; }

  .page { position: absolute; left: 99px; top: 0; width: 1002px; height: 902px; background: var(--panel-bg); border: 1px solid var(--panel-line); border-top: none; }

  .site-header { height: 109px; position: relative; }
  .brand { position: absolute; left: 20px; top: 34px; font-family: "Questrial", sans-serif; font-weight: 400; color: var(--navy); font-size: 34px; letter-spacing: .5px; }

  .main-nav { display: flex; height: 49px; margin: 0 1px; background: linear-gradient(var(--navy-light), var(--navy-dark)); }
  .main-nav a { color: #fff; text-decoration: none; font-weight: 700; font-size: 15px; display: flex; align-items: center; justify-content: center; border-right: 1px solid rgba(255,255,255,.25); }
  .main-nav a:last-child { border-right: none; flex: 1; }

  .hero { position: relative; height: 462px; margin: 0 1px; border-bottom: 1px solid var(--panel-line); overflow: hidden; }
  .hero-visual { position: absolute; left: 280px; top: 36px; width: 720px; height: 390px;
    background: radial-gradient(ellipse at 55% 55%, #efe7e4 0%, #f6f1ef 40%, #ffffff 72%); }
  .hero-copy { position: absolute; left: 68px; top: 155px; width: 640px; }
  .hero-title { font-family: "Questrial", sans-serif; font-weight: 400; color: var(--heading); font-size: 35px; line-height: 42px; white-space: nowrap; }
  .hero-subtitle { font-family: "Questrial", sans-serif; font-weight: 400; color: var(--subheading); font-size: 20px; line-height: 26px; margin-top: 2px; }
  .hero-text { font-weight: 300; font-size: 12.5px; line-height: 22px; margin-top: 6px; color: #7c7c7c; }
  .slider-dots { display: flex; gap: 3px; margin-top: 9px; }
  .slider-dots span { width: 13px; height: 13px; border-radius: 50%; background: var(--dot); }

  .features { position: relative; height: 265px; }
  .about { position: absolute; left: 29px; top: 44px; width: 310px; }
  .about h2 { font-family: "Questrial", sans-serif; font-weight: 400; color: var(--heading); font-size: 25px; margin-bottom: 6px; }
  .about p { font-weight: 300; font-size: 13px; line-height: 21.5px; color: var(--body-text); margin-bottom: 8px; }

  .video-tile { position: absolute; left: 349px; top: 42px; width: 224px; height: 163px;
    background: linear-gradient(135deg, #bfe6f7 0%, #4fa9dc 45%, #1d6fb5 75%, #8fd0f0 100%); }
  .play-button { position: absolute; left: 95px; top: 65px; }

  .product-card { position: absolute; top: 41px; width: 184px; }
  .product-card.fashion { left: 594px; }
  .product-card.industry { left: 791px; }
  .product-image { height: 92px; border: 1px solid var(--panel-line); }
  .fashion .product-image { background: linear-gradient(120deg, #f7d7df 0%, #ea3c6c 45%, #c9134a 80%, #f5e1e6 100%); }
  .industry .product-image { background: linear-gradient(120deg, #eeeeee 0%, #d9c98f 45%, #c6a651 70%, #ececec 100%); }
  .product-card h3 { font-weight: 400; font-size: 16.5px; color: var(--dark-text); margin: 12px 0 4px 4px; }
  .product-card p { font-weight: 300; font-size: 13px; line-height: 21.5px; margin-left: 4px; color: var(--body-text); }

  .site-footer { position: absolute; left: 119px; top: 928px; width: 978px; }
  .footer-nav { font-size: 14px; color: var(--footer-text); }
  .footer-nav a { color: var(--footer-text); text-decoration: none; }
  .footer-nav .sep { margin: 0 6px; }
  .copyright { font-weight: 300; font-size: 13px; color: var(--footer-text); margin-top: 14px; }
  .social { position: absolute; right: 0; top: 2px; display: flex; gap: 6px; }
  .social span { width: 22px; height: 22px; border-radius: 50%; background: #777; }
</style>
</head>
<body>
  <div class="page">
    <header class="site-header">
      <div class="brand">Orvane</div>
    </header>

    <nav class="main-nav">
      <a href="#" style="width:111px">HOME</a>
      <a href="#" style="width:135px">ABOUT US</a>
      <a href="#" style="width:179px">CORE PRODUCTS</a>
      <a href="#" style="width:122px">SERVICES</a>
      <a href="#" style="width:204px">RISK MANAGEMENT</a>
      <a href="#" style="width:117px">CLIENTS</a>
      <a href="#">CONTACT</a>
    </nav>

    <section class="hero">
      <div class="hero-visual" role="img" aria-label="Cosmetics still life: eyeshadow compact, lip gloss and powder compact with puff"></div>
      <div class="hero-copy">
        <h1 class="hero-title">Orvane Ladies Fashion Products</h1>
        <p class="hero-subtitle">Phasellus felis dolor scelerisque empus</p>
        <p class="hero-text">Sed porta Suspendisse quam leo molestie sed luctus quis feugiat in pede<br>Fusce tellus Sed metus augue convallis et vehicula</p>
        <div class="slider-dots"><span></span><span></span><span></span><span></span></div>
      </div>
    </section>

    <section class="features">
      <div class="about">
        <h2>About Our Company</h2>
        <p>Sed porta Suspendisse quam leo molestie sed luctus quis feugiat in pede Fusce tellus Sed metus augue convallis et vehicula ut pulvinar eu ante Integer orci Maecenas at justo id velit placerat molestie</p>
        <p>Donec dictum lectus non odio Cras a ante vitae enim iaculis aliquam Mauris nunc quam venenatis</p>
      </div>

      <div class="video-tile" role="img" aria-label="Video thumbnail: glowing blue globe with network lines">
        <svg class="play-button" width="34" height="34" viewBox="0 0 34 34" aria-hidden="true">
          <circle cx="17" cy="17" r="17" fill="#1b1b1b"/>
          <path d="M13 10 L24 17 L13 24 Z" fill="#fff"/>
        </svg>
      </div>

      <div class="product-card fashion">
        <div class="product-image" role="img" aria-label="Pink handbag and high-heeled shoe"></div>
        <h3>Fashion Products</h3>
        <p>Allis et vehicula ut pulvinar eu ante Integer orci Tellus</p>
      </div>

      <div class="product-card industry">
        <div class="product-image" role="img" aria-label="Gold jewelled wristwatch"></div>
        <h3>Industry Products</h3>
        <p>Allis et vehicula ut pulvinar eu ante Integer orci Tellus</p>
      </div>
    </section>
  </div>

  <footer class="site-footer">
    <nav class="footer-nav">
      <a href="#">HOME</a><span class="sep">/</span><a href="#">ABOUT US</a><span class="sep">/</span><a href="#">CORE PRODUCTS</a><span class="sep">/</span><a href="#">SERVICES</a><span class="sep">/</span><a href="#">RISK MANAGEMENT</a><span class="sep">/</span><a href="#">CLIENTS</a><span class="sep">/</span><a href="#">CONTACT</a>
    </nav>
    <p class="copyright">© 2014 Company Name&nbsp; All right reserved&nbsp; Term of Use</p>
    <div class="social" aria-label="Social links"><span></span><span></span><span></span></div>
  </footer>
</body>
</html>
```